Maple Burrow Canine Massage Needs a Business Card Design

Maple Burrow Canine Massage is a new therapeutic canine massage company located in Nederland, Colorado. I need a business card design that include my logo and basic contact information.

Target Market(s)

Pet owners, veterinarians

Industry/Entity Type

Business

Contact Information for Business Card

Tessa Lindqvist, CCMT
303.581.7296
tessa@mapleburrowmassage.example
www.mapleburrowmassage.example

Colors
6c459b
886aae
b8a6cd
a64599
b768aa
d3a5cc
fbed22

Requirements
Must have
• Font should be similar to font in logo.

```html
<!DOCTYPE html>
<html lang="en">
<head>
<meta charset="utf-8">
<title>Maple Burrow Canine Massage – Business Card</title>
<link href="https://fonts.googleapis.com/css2?family=Source+Sans+3:wght@400;500;600&display=swap" rel="stylesheet">
<style>
  :root {
    --stage: #141414;
    --card: #ffffff;
    --purple-deep: #6c459b;
    --purple-mid: #886aae;
    --lavender: #b8a6cd;
    --magenta: #a64599;
    --orchid: #b768aa;
    --pink-light: #d3a5cc;
    --yellow: #fbed22;
    --ring: #f3d86a;
  }
  * { margin: 0; padding: 0; box-sizing: border-box; }
  html, body {
    width: 1200px; height: 904px; overflow: hidden;
    background: var(--stage);
    font-family: "Source Sans 3", "Myriad Pro", sans-serif;
  }
  .stage { position: relative; width: 1200px; height: 904px; }
  .card {
    position: absolute;
    left: 50px; top: 139.5px;
    width: 912px; height: 518px;
    background: var(--card);
    transform: scale(1.2061);
    transform-origin: 0 0;
    overflow: hidden;
  }
  .chevron { position: absolute; inset: 0; width: 912px; height: 518px; }
  .brand-mark {
    position: absolute;
    left: 55px; top: 119px;
    width: 294px; height: 294px;
    border-radius: 50%;
    border: 4px solid var(--ring);
    background: linear-gradient(180deg, var(--lavender) 0%, #c9a6d6 60%, var(--purple-deep) 100%);
    display: flex; align-items: center; justify-content: center;
  }
  .brand-mark__name {
    font-weight: 600; font-size: 30px; color: var(--yellow);
    text-align: center; line-height: 1.1; letter-spacing: 0.5px;
  }
  .company {
    position: absolute; right: 38px; top: 78px;
    font-size: 41px; font-weight: 500; color: var(--orchid);
    white-space: nowrap;
  }
  .person {
    position: absolute; right: 38px; top: 284px;
    font-size: 35px; font-weight: 500; color: var(--magenta);
    white-space: nowrap;
  }
  .contact { position: absolute; right: 38px; top: 352px; list-style: none; }
  .contact__item {
    display: flex; align-items: center; justify-content: flex-end;
    height: 37px; gap: 27px;
  }
  .contact__text { font-size: 23px; color: var(--orchid); opacity: 0.8; white-space: nowrap; }
  .contact__icon { width: 32px; height: 32px; background: var(--yellow); display: block; }
</style>
</head>
<body>
<main class="stage">
  <section class="card" aria-label="Business card">
    <svg class="chevron" viewBox="0 0 912 518" aria-hidden="true">
      <polygon points="215,0 255,0 481,265" fill="var(--pink-light)"/>
      <polygon points="481,265 226,518 258,518" fill="var(--orchid)"/>
    </svg>

    <div class="brand-mark">
      <span class="brand-mark__name">Maple<br>Burrow</span>
    </div>

    <h1 class="company">Maple Burrow Canine Massage</h1>
    <p class="person">Tessa Lindqvist, CCMT</p>

    <ul class="contact">
      <li class="contact__item">
        <span class="contact__text">303.581.7296</span>
        <svg class="contact__icon" viewBox="0 0 32 32" aria-label="Phone">
          <rect width="32" height="32" fill="var(--yellow)"/>
          <path d="M7 14c0-4 4-6 9-6s9 2 9 6h-4v-2h-10v2z" fill="#fff" stroke="var(--orchid)" stroke-width="1.2"/>
          <rect x="8" y="15" width="16" height="9" rx="2" fill="#fff" stroke="var(--orchid)" stroke-width="1.2"/>
        </svg>
      </li>
      <li class="contact__item">
        <span class="contact__text">tessa@mapleburrowmassage.example</span>
        <svg class="contact__icon" viewBox="0 0 32 32" aria-label="Email">
          <rect width="32" height="32" fill="var(--yellow)"/>
          <rect x="6" y="9" width="20" height="14" fill="#fff" stroke="var(--orchid)" stroke-width="1.4"/>
          <path d="M6 9l10 8 10-8M6 23l8-7M26 23l-8-7" fill="none" stroke="var(--orchid)" stroke-width="1.4"/>
        </svg>
      </li>
      <li class="contact__item">
        <span class="contact__text">www.mapleburrowmassage.example</span>
        <svg class="contact__icon" viewBox="0 0 32 32" aria-label="Website">
          <rect width="32" height="32" fill="var(--yellow)"/>
          <circle cx="16" cy="16" r="10" fill="#fff" stroke="var(--orchid)" stroke-width="1.4"/>
          <path d="M6 16h20M16 6c-5 5-5 15 0 20M16 6c5 5 5 15 0 20" fill="none" stroke="var(--orchid)" stroke-width="1.2"/>
        </svg>
      </li>
    </ul>
  </section>
</main>
</body>
</html>
```